Sleek Design For Personal Brand Wordpress Website !!

*WORDPRESS WEBSITE*

Need a sleek and easy to navigate Wordpress website.

It will act as the hub for my personal brand.

Which means it will showcase all my social media outlets, host my most recent content like youtube videos and podcasts...

It will also be the go to place to find all my digital products and services that I offer.

i want it to be super sleek and simple but also give a personal touch of my who I really am. You can get a good idea of who I am my checking out my Instagram (@karel.dumonte)

Use these websites for ideas: www.brevanhollis.example and www.dorianfelkowitz.example

Target Market(s)

Young Entrepreneurs

Industry/Entity Type

Education

Logo Text

Karel Dumonte

Number of Pages Required

4 page

Font styles to use
Sans Serif

Colors
ffffff
0392cd
ec1f27

Requirements
Must have
• Social Media buttons on the home page...
• Video (also a slider) right at the top of the home page...
• Email Optin...
• Multiple pages...

```html
<!DOCTYPE html>
<html lang="en">
<head>
<meta charset="utf-8">
<title>Karel Dumonte</title>
<link rel="stylesheet" href="https://fonts.googleapis.com/css2?family=Open+Sans:ital,wght@0,400;0,600;0,700;1,400;1,700&family=Questrial&display=swap">
<style>
:root{
  --blue:#0392cd;
  --red:#ec1f27;
  --white:#ffffff;
  --ink:#1a1a1a;
  --text:#444444;
  --muted:#666666;
  --panel:#e4e4e4;
  --field:#c9c9c9;
  --footer:#000000;
}
*{box-sizing:border-box;margin:0;padding:0}
html,body{width:1200px;height:3005px;overflow:hidden}
body{position:relative;background:var(--white);font-family:"Questrial",sans-serif;color:var(--text)}
.abs{position:absolute}
.heading{font-family:"Open Sans",sans-serif;font-weight:700;color:var(--ink);letter-spacing:.5px}
.photo{position:absolute}

/* header */
.brand{left:200px;top:22px;display:flex;align-items:center;gap:10px;font-family:"Open Sans",sans-serif;font-size:24px;color:var(--ink)}
.brand-mark{width:14px;height:14px;background:var(--blue)}
.nav{left:434px;top:26px;display:flex;font-family:"Open Sans",sans-serif;font-size:13px;font-weight:600;color:var(--ink)}
.nav a{color:inherit;text-decoration:none;display:block;height:34px;line-height:34px;padding:0 12px;margin-right:20px}
.nav a.active{background:var(--blue);color:var(--white);padding:0 14px}

/* hero */
.hero-bg{left:40px;top:90px;width:1160px;height:580px;background:linear-gradient(135deg,#f2f2f2,#e2e2e2 55%,#efefef)}
.hero-title{left:200px;top:118px;font-size:30px;line-height:36px;text-transform:uppercase;color:#2a2a2a}
.hero-photo{left:0;top:210px;width:740px;height:402px;background:linear-gradient(120deg,#2b3340,#121821 55%,#3a3f45)}
.hero-tag{left:200px;top:378px;width:270px;font-family:"Open Sans",sans-serif;font-style:italic;font-weight:700;font-size:13px;line-height:20px;color:var(--white)}
.btn{position:absolute;height:38px;line-height:38px;text-align:center;font-family:"Open Sans",sans-serif;font-weight:700;font-size:11px;color:var(--white);text-transform:uppercase}
.btn-blue{background:var(--blue)}
.btn-red{background:var(--red)}
.video{left:612px;top:272px;width:486px;height:280px;background:linear-gradient(160deg,#6f8496,#3d5066 50%,#8a8fb8)}
.play{left:782px;top:394px;width:44px;height:36px;border:3px solid var(--red)}

/* section head */
.rule{position:absolute;height:2px;background:#cfcfcf}
.section-title{position:absolute;left:0;width:1200px;text-align:center;font-size:28px}
.lede{position:absolute;left:290px;width:620px;text-align:center;font-style:italic;font-size:15px;line-height:24px;color:var(--muted)}

/* features */
.back-panel{position:absolute;background:var(--panel)}
.frame{position:absolute;border:1.5px solid rgba(255,255,255,.85)}
.feature-title{position:absolute;font-size:28px;line-height:34px;text-transform:uppercase}
.feature-sub{position:absolute;font-family:"Open Sans",sans-serif;font-style:italic;font-weight:700;font-size:13px;line-height:18px;color:var(--ink);text-transform:uppercase}
.feature-body{position:absolute;font-size:13px;line-height:22px;color:var(--text)}
.read-more{position:absolute;font-family:"Open Sans",sans-serif;font-weight:700;font-size:11px;color:var(--ink)}

/* social */
.social-tile{position:absolute;width:46px;height:46px;background:var(--red);border-radius:4px;display:flex;align-items:center;justify-content:center;font-family:"Open Sans",sans-serif;font-weight:700;font-size:10px;color:var(--white);text-decoration:none}
.social-note{position:absolute;width:180px;text-align:center;font-size:12px;line-height:20px;color:var(--text)}

/* contact */
.field{position:absolute;top:2492px;height:42px;background:var(--field);border-radius:4px;font-style:italic;font-size:13px;line-height:42px;padding-left:18px;color:#555}
.submit{position:absolute;left:870px;top:2492px;width:128px;height:42px;background:var(--blue);border-radius:4px;color:var(--white);font-family:"Open Sans",sans-serif;font-weight:700;font-size:12px;text-align:center;line-height:42px;text-transform:uppercase}

/* newsletter */
.newsletter{left:0;top:2612px;width:1200px;height:126px;background:var(--blue)}
.newsletter-title{left:198px;top:2646px;font-family:"Open Sans",sans-serif;font-weight:700;font-size:24px;color:var(--white);text-transform:uppercase}
.newsletter-sub{left:200px;top:2686px;font-style:italic;font-size:15px;color:var(--white)}
.newsletter-input{left:626px;top:2654px;width:248px;height:40px;background:var(--white);border-radius:4px;font-size:12px;line-height:40px;padding-left:12px;color:#555}
.newsletter-btn{left:884px;top:2654px;width:114px;height:40px;border:1.5px solid var(--white);border-radius:4px;font-family:"Open Sans",sans-serif;font-weight:700;font-size:12px;color:var(--white);text-align:center;line-height:38px;text-transform:uppercase}

/* footer */
.footer{left:0;top:2738px;width:1200px;height:267px;background:var(--footer)}
.footer-map{left:400px;top:2760px;width:560px;height:230px;background:radial-gradient(ellipse at center,#2a2a2a,#111 60%,#000 80%)}
.footer-brand{left:200px;top:2786px;display:flex;align-items:center;gap:10px;font-family:"Open Sans",sans-serif;font-size:24px;color:var(--white)}
.footer-brand .brand-mark{background:var(--white)}
.footer-social{position:absolute;top:2850px;width:30px;height:30px;border-radius:50%;background:var(--red);display:flex;align-items:center;justify-content:center;font-family:"Open Sans",sans-serif;font-weight:700;font-size:8px;color:var(--white);text-decoration:none}
.copyright{left:200px;top:2898px;font-size:12px;line-height:20px;color:var(--white)}
.footer-heading{position:absolute;top:2796px;font-family:"Open Sans",sans-serif;font-style:italic;font-weight:700;font-size:17px;color:var(--white)}
.footer-underline{position:absolute;top:2830px;height:2px;background:var(--red)}
.footer-text{position:absolute;font-size:12px;line-height:20px;color:var(--white)}
.footer-icon{position:absolute}
</style>
</head>
<body>

<header>
  <div class="abs brand"><span class="brand-mark"></span>Karel Dumonte</div>
  <nav class="abs nav">
    <a class="active" href="#">Home</a>
    <a href="#">About</a>
    <a href="#">Podcast</a>
    <a href="#">Events</a>
    <a href="#">Hire me to Speak</a>
    <a href="#">Contact Us</a>
  </nav>
</header>

<section class="hero">
  <div class="abs hero-bg"></div>
  <h1 class="abs heading hero-title">We will take you by the hand to show you exactly<br>how we did it!</h1>
  <div class="photo hero-photo" role="img" aria-label="Photo of the brand owner standing beside a white sports car at a petrol station at night"></div>
  <p class="abs hero-tag">We Will Teach You Step-By-Step How We Went From $0 to $226K A Month On Storefy!</p>
  <a class="btn btn-blue" style="left:198px;top:444px;width:152px">Get Started Now</a>
  <a class="btn btn-red" style="left:362px;top:444px;width:152px">Contact Us</a>
  <div class="photo video" role="img" aria-label="Video still of the brand owner in sunglasses in front of city towers"></div>
  <div class="abs play"></div>
  <svg class="abs" style="left:798px;top:403px" width="14" height="18" viewBox="0 0 14 18"><path d="M1 1 L13 9 L1 17 Z" fill="#ec1f27"/></svg>
</section>

<section class="welcome">
  <div class="rule" style="left:570px;top:744px;width:60px"></div>
  <h2 class="heading section-title" style="top:750px">WELCOME</h2>
  <p class="lede" style="top:808px">Vestibulum at magna tellus. Vivamus sagittis et nunc ut in orci aliquam, ac vulputa leo vehicul Mauris Vivamus sagittis et nunc ut in orci aliquam...</p>
</section>

<section class="feature feature-learn">
  <div class="back-panel" style="left:750px;top:962px;width:450px;height:410px"></div>
  <div class="photo" style="left:598px;top:920px;width:550px;height:410px;background:linear-gradient(135deg,#cfc8bc,#a89f92 50%,#6d6a63)" role="img" aria-label="Photo of the brand owner in a bright living room with an indoor pond"></div>
  <div class="frame" style="left:622px;top:938px;width:556px;height:374px"></div>
  <div class="rule" style="left:200px;top:988px;width:116px"></div>
  <h2 class="heading feature-title" style="left:200px;top:1000px">What you will learn<br>on this free<br>training</h2>
  <p class="feature-sub" style="left:200px;top:1124px">How you create a Storefy store<br>that converts</p>
  <p class="feature-body" style="left:200px;top:1174px;width:330px">Building an eCommerce store is simple but building a store thatactually makes people want to buy is more important!</p>
  <p class="read-more" style="left:200px;top:1252px">READ MORE &#10148;</p>
</section>

<section class="feature feature-reveals">
  <div class="back-panel" style="left:0;top:1410px;width:452px;height:412px"></div>
  <div class="photo" style="left:50px;top:1370px;width:550px;height:412px;background:linear-gradient(135deg,#5b6a6e,#9aa7a6 45%,#3d4848)" role="img" aria-label="Photo of the brand owner in a white jacket in front of a glass building"></div>
  <div class="frame" style="left:20px;top:1388px;width:560px;height:374px"></div>
  <div class="rule" style="left:960px;top:1458px;width:38px"></div>
  <h2 class="heading feature-title" style="left:698px;top:1470px;width:300px;text-align:right">Free<br>training<br>reveals</h2>
  <p class="feature-sub" style="left:598px;top:1592px;width:400px;text-align:right">Lorem ipsum is simply dummy text<br>of the printing industry</p>
  <p class="feature-body" style="left:678px;top:1642px;width:320px;text-align:right">Lorem Ipsum is simply dummy text of the printing and typesetting industry. Lorem Ipsum has been the industry's standard dummy text...</p>
  <p class="read-more" style="left:898px;top:1718px;width:100px;text-align:right">READ MORE &#10148;</p>
</section>

<section class="feature feature-social">
  <div class="back-panel" style="left:750px;top:1868px;width:450px;height:410px"></div>
  <div class="photo" style="left:598px;top:1826px;width:550px;height:410px;background:linear-gradient(135deg,#9fb0c0,#c9c6b8 40%,#5b5132 80%)" role="img" aria-label="Photo of the brand owner seated in the open door of a helicopter"></div>
  <div class="frame" style="left:622px;top:1846px;width:526px;height:370px"></div>
  <div class="rule" style="left:200px;top:1892px;width:68px"></div>
  <h2 class="heading feature-title" style="left:200px;top:1906px;font-size:27px">Stay in touch<br>with me</h2>
  <a class="social-tile" href="#" style="left:240px;top:2006px" aria-label="Main social feed">Feed</a>
  <a class="social-tile" href="#" style="left:450px;top:2006px" aria-label="Photo profile">Photos</a>
  <p class="social-note" style="left:174px;top:2066px">My biggest platform. Join the Hollisnation &amp; stay up to</p>
  <p class="social-note" style="left:384px;top:2066px">My favorite place. Quotes, stories &amp; your chance to win</p>
  <a class="social-tile" href="#" style="left:240px;top:2120px" aria-label="Business profile">Work</a>
  <a class="social-tile" href="#" style="left:450px;top:2120px" aria-label="Podcast">Listen</a>
  <p class="social-note" style="left:174px;top:2180px">My business profile. Hollis Media is hiring/date do.</p>
  <p class="social-note" style="left:384px;top:2180px">Perfect for your commute. Listen daily to keynotes. inter-</p>
</section>

<section class="contact">
  <div class="rule" style="left:512px;top:2336px;width:56px"></div>
  <h2 class="heading section-title" style="top:2344px">CONTACT US</h2>
  <p class="lede" style="top:2408px">Vestibulum at magna tellus. Vivamus sagittis et nunc ut in orci aliquam, ac vulputa leo vehicul Mauris Vivamus sagittis et nunc ut in orci aliquam...</p>
  <div class="field" style="left:200px;width:206px">Name</div>
  <div class="field" style="left:424px;width:206px">Email</div>
  <div class="field" style="left:646px;width:206px">Subject</div>
  <div class="submit">Submit</div>
</section>

<section class="newsletter-band">
  <div class="abs newsletter"></div>
  <h2 class="abs newsletter-title">Sign up for a newsletter...</h2>
  <p class="abs newsletter-sub">...and never miss our specila Updates and news !</p>
  <div class="abs newsletter-input">Enter Your E-mail</div>
  <div class="abs newsletter-btn">Subscribe !</div>
</section>

<footer>
  <div class="abs footer"></div>
  <div class="abs footer-map" role="img" aria-label="Faint world map backdrop"></div>
  <div class="abs footer-brand"><span class="brand-mark"></span>Karel Dumonte</div>
  <a class="footer-social" href="#" style="left:200px" aria-label="Main social feed">Feed</a>
  <a class="footer-social" href="#" style="left:238px" aria-label="Short posts">Post</a>
  <a class="footer-social" href="#" style="left:276px" aria-label="Pinned boards">Pins</a>
  <a class="footer-social" href="#" style="left:314px" aria-label="More networks">Plus</a>
  <p class="abs copyright">© Copyright 2017 karel dumonte.<br>All Rights Reserved.</p>

  <h3 class="footer-heading" style="left:454px">Keep in Touch</h3>
  <div class="footer-underline" style="left:454px;width:150px"></div>
  <svg class="footer-icon" style="left:456px;top:2856px" width="14" height="14" viewBox="0 0 14 14"><path d="M3 1 L5 1 L6 4 L4.5 5.5 Q6 8.5 8.5 9.5 L10 8 L13 9 L13 11 Q13 13 11 13 Q1 12 1 3 Q1 1 3 1 Z" fill="#ec1f27"/></svg>
  <p class="footer-text" style="left:484px;top:2854px">+1234567891</p>
  <svg class="footer-icon" style="left:457px;top:2886px" width="12" height="16" viewBox="0 0 12 16"><path d="M6 0 A6 6 0 0 1 12 6 Q12 10 6 16 Q0 10 0 6 A6 6 0 0 1 6 0 Z M6 3.5 A2.5 2.5 0 1 0 6 8.5 A2.5 2.5 0 1 0 6 3.5 Z" fill="#ec1f27" fill-rule="evenodd"/></svg>
  <p class="footer-text" style="left:484px;top:2884px;width:180px">Lorem Ipsum is simply dummy<br>of the printing</p>
  <svg class="footer-icon" style="left:455px;top:2944px" width="16" height="12" viewBox="0 0 16 12"><rect x="0.5" y="0.5" width="15" height="11" fill="none" stroke="#ec1f27"/><path d="M0.5 0.5 L8 7 L15.5 0.5" fill="none" stroke="#ec1f27"/></svg>
  <p class="footer-text" style="left:484px;top:2940px">info@kareldumonte.example</p>

  <h3 class="footer-heading" style="left:716px">Quick Links</h3>
  <div class="footer-underline" style="left:716px;width:130px"></div>
  <p class="footer-text" style="left:716px;top:2856px;line-height:24px">Home<br>About<br>Podcast<br>Events</p>
  <p class="footer-text" style="left:902px;top:2856px;line-height:24px">Hire Me to Speak<br>Contact Us<br>Help</p>
</footer>

</body>
</html>
```